Packaging design for Quarry Bloom Premium Extra Virgin Olive Oil

Based on our label design, we need a whole packaging design for our product, which includes bottle and gift pack design.

Ideally we prefer the shape of Morvela bottle, please refer to the picture that I uploaded. With cork or screw neck finish, bottle must be in antique green, dark green or amber colour. However, any other ideas will be appreciated, as long as it looks great.

The gift pack design is quite open, personally I prefer the paper tube package. we uploaded some sample designs that we like for your reference. Please feel free to use the actual logos and barcode for our product attached in brief files.

For practical reason, we prefer to use 250ml Morvela glass bottle, please see the dimention details below, regarding to the bottle shape please refer to my sample picture.
Capacity: 250 ml
Weight: 250 grs
Diameter: 54,10 mm
Height: 250,80 mm

Requirements
Must have
• Quarry Bloom Olive Oil Logo.
"Fall 2014 Harvest"
Barcode
Product of Australia Logo
Kestrel Cold Press Certified Logo

```html
<!DOCTYPE html>
<html lang="en">
<head>
<meta charset="utf-8">
<title>Quarry Bloom Olive Oil Packaging</title>
<link rel="stylesheet" href="https://fonts.googleapis.com/css2?family=Marcellus&family=Open+Sans:wght@400;600;700&display=swap">
<style>
  :root {
    --backdrop: #2b2b2b;
    --cream: #f4f1e4;
    --olive-green: #3f7b55;
    --sage: #5f9471;
    --glass: #5b5e2c;
    --glass-dark: #3a3d1c;
    --cap: #1f3a22;
    --box-white: #ecebe6;
    --box-shade: #d9d8d2;
    --text-light: #ffffff;
  }
  html, body {
    margin: 0;
    width: 1200px;
    height: 1172px;
    overflow: hidden;
    background: var(--backdrop);
  }
  .canvas {
    position: relative;
    width: 1200px;
    height: 1172px;
    background: radial-gradient(ellipse at 50% 45%, #333 0%, var(--backdrop) 70%);
  }
  .bottle {
    position: absolute;
    left: 0;
    top: 0;
    width: 1200px;
    height: 1172px;
  }
  .label {
    position: absolute;
    left: 352px;
    top: 532px;
    width: 194px;
    height: 458px;
    background: var(--cream);
    overflow: hidden;
    font-family: "Open Sans", sans-serif;
  }
  .brand-mark {
    position: absolute;
    left: 0;
    right: 0;
    display: flex;
    flex-direction: column;
    align-items: center;
    text-align: center;
    color: var(--olive-green);
  }
  .brand-mark .dot {
    border-radius: 50%;
    background: var(--olive-green);
  }
  .brand-mark .name {
    font-family: "Marcellus", serif;
    line-height: 1.1;
  }
  .brand-mark .kind {
    font-family: "Open Sans", sans-serif;
    font-weight: 700;
    letter-spacing: 1px;
  }
  .brand-mark .producer { font-family: "Open Sans", sans-serif; }
  .label .brand-mark { top: 22px; }
  .label .dot { width: 14px; height: 14px; margin-bottom: 20px; }
  .label .name { font-size: 20px; }
  .label .kind { font-size: 9px; margin-top: 6px; }
  .label .producer { font-size: 5.5px; margin-top: 4px; }
  .label .grade {
    position: absolute;
    left: 0;
    right: 0;
    top: 146px;
    text-align: center;
    font-family: "Marcellus", serif;
    color: var(--olive-green);
    line-height: 1;
  }
  .label .grade .premium { font-size: 35px; }
  .label .grade .extra { font-size: 21px; margin-top: 1px; }
  .label .lower-panel {
    position: absolute;
    left: 0;
    top: 300px;
    width: 194px;
    height: 158px;
    background: var(--sage);
  }
  .label .branch-art {
    position: absolute;
    left: 0;
    top: 226px;
    width: 194px;
    height: 104px;
    background: linear-gradient(180deg, #d6ddd0 0%, #86ac8f 45%, var(--sage) 100%);
  }
  .label .story {
    position: absolute;
    left: 12px;
    right: 12px;
    top: 338px;
    margin: 0;
    font-size: 7px;
    line-height: 1.4;
    color: var(--text-light);
    text-align: justify;
    text-align-last: center;
  }
  .label .volume {
    position: absolute;
    left: 0;
    right: 0;
    top: 414px;
    text-align: center;
    font-family: "Open Sans", sans-serif;
    font-weight: 700;
    font-size: 14px;
    color: var(--text-light);
  }
  .label .volume-rule {
    position: absolute;
    top: 424px;
    width: 26px;
    height: 2px;
    background: var(--olive-green);
  }
  .label .volume-rule.left { left: 16px; }
  .label .volume-rule.right { right: 16px; }
  .label .base-band {
    position: absolute;
    left: 0;
    bottom: 0;
    width: 194px;
    height: 8px;
    background: var(--olive-green);
  }
  .gift-box {
    position: absolute;
    left: 622px;
    top: 145px;
    width: 284px;
    height: 868px;
    background: linear-gradient(100deg, var(--box-shade) 0%, var(--box-white) 30%, #f2f1ec 60%, var(--box-shade) 100%);
  }
  .gift-box .side-edge {
    position: absolute;
    left: 0;
    top: 0;
    width: 16px;
    height: 868px;
    background: linear-gradient(180deg, #e2e1dc 0%, #eed9dc 100%);
  }
  .gift-box .brand-mark { top: 418px; }
  .gift-box .dot { width: 22px; height: 22px; margin-bottom: 14px; }
  .gift-box .name { font-size: 28px; }
  .gift-box .kind { font-size: 13px; margin-top: 10px; }
  .gift-box .producer { font-size: 7px; margin-top: 6px; }
</style>
</head>
<body>
<main class="canvas">
  <svg class="bottle" viewBox="0 0 1200 1172" aria-label="Antique green glass bottle">
    <defs>
      <linearGradient id="glass-tone" x1="0" x2="1" y1="0" y2="0">
        <stop offset="0" stop-color="#3a3d1c"/>
        <stop offset="0.35" stop-color="#6a6d35"/>
        <stop offset="0.7" stop-color="#5b5e2c"/>
        <stop offset="1" stop-color="#33361a"/>
      </linearGradient>
    </defs>
    <path d="M404 330 L404 395 C404 450 338 470 338 540 L338 1000 Q338 1012 352 1012 L532 1012 Q546 1012 546 1000 L546 540 C546 470 480 450 480 395 L480 330 Z" fill="url(#glass-tone)"/>
    <path d="M402 210 Q402 198 414 198 L470 198 Q482 198 482 210 L482 335 L402 335 Z" fill="var(--cap)"/>
    <rect x="400" y="216" width="84" height="6" fill="#2c4a2e"/>
  </svg>

  <section class="label" aria-label="Bottle label">
    <div class="brand-mark">
      <span class="dot"></span>
      <span class="name">Quarry Bloom</span>
      <span class="kind">OLIVE OIL</span>
      <span class="producer">Proudly produced by Harlow Ridge Estate</span>
    </div>
    <div class="grade">
      <div class="premium">PREMIUM</div>
      <div class="extra">EXTRA VIRGIN</div>
    </div>
    <div class="lower-panel"></div>
    <div class="branch-art" role="img" aria-label="Sketched olive branches and an olive tree over a green brush wash"></div>
    <p class="story">Nested in the Greater Bendigo region of Victoria, Harlow Ridge Estate represents one of the freshest and finest extra virgin olive oils in Australia. Blessed by Central Victoria's Mediterranean climate, our extra virgin olive oils feature a crisp, distinctive taste of freshness and fruity aromas.</p>
    <span class="volume-rule left"></span>
    <div class="volume">375 ml</div>
    <span class="volume-rule right"></span>
    <div class="base-band"></div>
  </section>

  <section class="gift-box" aria-label="Gift box front">
    <div class="side-edge"></div>
    <div class="brand-mark">
      <span class="dot"></span>
      <span class="name">Quarry Bloom</span>
      <span class="kind">OLIVE OIL</span>
      <span class="producer">Proudly produced by Harlow Ridge Estate</span>
    </div>
  </section>
</main>
</body>
</html>
```